Psychologist in Private Practice Needs a Website Update

Project Description:
Hello talented designers! My current website, www.junetillard.com, needs a fresh, boho-modern makeover that highlights the warm, welcoming nature of my holistic therapy practice. I want a website that has a serene, boho- modern design, appealing to clients seeking individual therapy, couples therapy, and family counseling.

I’d also like to prepare for a future second site focused exclusively on couples and family therapy. Both sites should be interconnected, so I’m looking for design suggestions that seamlessly link them together while maintaining a cohesive brand look and feel.

Key Objectives:

Boho-Modern Aesthetic: Incorporate natural textures, neutral or earthy tones, and clean lines that capture a modern, inviting vibe.

Responsive Design: Ensure the website is user-friendly on desktop, tablet, and mobile devices.

Clear Service Offerings: Prominently feature my three distinct services: individual therapy, couples therapy, and family counseling.

Interlinked Future Site: Provide ideas on how to cross-link this site with a second site focused on couples and family therapy.

User Experience (UX): Make the site simple to navigate, with intuitive placement of content that speaks to potential clients’ needs.

SEO-Friendly: Implement best practices for structure, site speed, and keyword usage to boost online visibility.

What I Have Now:
Existing website: www.junetillard.com
Basic content and a logo that can be refined or updated to match the boho-modern feel
Rough style guide with brand elements open to a fresh interpretation

Preferred Style/Tone:
Boho-modern with earthy tones, subtle textures, and clean typography
Warm, empathetic, and approachable to align with the nature of therapy services
Slightly artistic or organic elements that evoke calm and connection

Potential for an ongoing design relationship!
Updates

Need extra days to review

Target Market(s)

I have a high functioning, professional clientele who doctors, lawyers, and leaders in their field.

Industry/Entity Type

healthcare/mental health

Coding

Coded - Design and coding required

Font styles to use
Other font styles liked:
• cormorant garamond for headers and Source Sans Pro for supporting text

Colors

Designer to choose colors to be used in the design.

Requirements
Must have
• Open, Harmonious Layout I’d like the overall design to feel upscale, humanistic, open and harmonious, with minimal divisions of space. Rather than traditional section dividers, please consider using images, subtle shifts in color, typography, or spacing to define sections. Hero Image & Inspiration Ideally, the first (hero) image should evoke a sense of awe or inspiration. Focus on simplicity and elegance so the design feels spacious and inviting, allowing the content and imagery to really stand out. Natural Flow Wherever possible, let the design elements flow naturally into each other, creating a sense of unity and cohesion throughout the site.
Nice to have
• 1. Full-Width Hero Image: • The homepage should feature a full-width hero image that extends edge-to-edge across the screen for a modern and visually immersive effect. • This image should set the tone for the website, reflecting a calming, humanistic/natural, and upscale feel. It could include subtle overlays or gradients to enhance readability of text and navigation elements. Ideally, this image should have one or two people in nature. The image could be slightly transparent to allow the text "holistic therapy" and the tagline "an integrative approach to transformation" to be easily visible. Please help me find a breath-taking image that evokes a sense of beauty, inspiration, awe or hope. 2. Menu Tabs Positioned Over the Image: • The menu tabs (navigation bar) should be positioned directly on top of the hero image, either centered or aligned to the top right/left, depending on the design. • The navigation bar should have a slightly transparent or solid background (depending on the image and visibility needs) to ensure the text is easily readable without detracting from the image. 3. Typography and Text Placement: • The text overlay on the hero image should use the selected fonts: • Cormorant Garamond for headers (e.g., the tagline or welcome message). • Source Sans Pro for any supporting text. 5. Seamless Transitions: • Below the full-width image, transitions into the next sections (like “About,” “Services,” or client-focused content) should be smooth, using full-width separators that maintain the cohesive, open layout style. 6. Color Palette: • A neutral and calming color palette should be used (e.g., soft blues, grays, whites, or very muted earth tones) to create a soothing atmosphere for visitors. This design approach ensures the homepage looks clean, modern, and professional while maintaining the calming and upscale aesthetic that reflects the values of my psychology practice

```html
<!DOCTYPE html>
<html lang="en">
<head>
<meta charset="utf-8">
<title>Dr. June Tillard — Holistic Therapy</title>
<link href="https://fonts.googleapis.com/css2?family=Cormorant+Garamond:ital,wght@0,400;0,500;0,600;1,400&family=Source+Sans+3:wght@400;600;700&display=swap" rel="stylesheet">
<style>
:root{
  --accent:#f0643c;
  --accent-soft:#f58a64;
  --ink:#2a2a2a;
  --muted:#6f6f6f;
  --white:#ffffff;
  --charcoal:#2b2b2b;
  --charcoal-deep:#222222;
  --panel:#333333;
  --navy:#1e2a3a;
  --line:#4a4a4a;
}
*{box-sizing:border-box;margin:0;padding:0}
html,body{width:1200px;height:3420px;overflow:hidden;background:var(--charcoal)}
body{font-family:"Source Sans 3",sans-serif;color:var(--white);position:relative}
.serif{font-family:"Cormorant Garamond",serif}

/* header */
.site-header{position:absolute;top:0;left:0;width:1200px;height:56px;background:var(--white);display:flex;align-items:center;justify-content:space-between;padding:0 56px 0 80px;z-index:2}
.brand-name{font-family:"Cormorant Garamond",serif;font-size:22px;font-weight:600;color:var(--ink);line-height:1}
.brand-role{font-size:11px;color:var(--muted);margin-top:2px}
.main-nav{display:flex;align-items:center;gap:34px}
.main-nav a{font-size:12px;font-weight:700;letter-spacing:1px;color:var(--ink);text-decoration:none}
.main-nav a.active{color:var(--accent)}
.social{display:flex;gap:8px;margin-left:8px}
.social span{width:18px;height:18px;border-radius:50%;background:var(--accent);display:block}

/* hero */
.hero{position:absolute;top:56px;left:0;width:1200px;height:664px}
.hero-photo{position:absolute;inset:0;background:linear-gradient(180deg,#2a3340 0%,#4a5560 30%,#6d6a60 45%,#3a3e38 65%,#1f2630 100%)}
.hero-copy{position:absolute;top:262px;left:0;width:100%;text-align:center}
.hero-title{font-family:"Cormorant Garamond",serif;font-size:64px;font-weight:500;color:var(--white);line-height:1}
.hero-tagline{font-family:"Cormorant Garamond",serif;font-size:22px;font-style:italic;margin-top:10px;color:#e8e8e8}

/* services */
.services{position:absolute;top:720px;left:0;width:1200px;height:840px;background:linear-gradient(180deg,#1f2a38 0%,#27313c 55%,var(--charcoal) 100%)}
.section-title{position:absolute;top:160px;width:100%;text-align:center;font-family:"Cormorant Garamond",serif;font-size:42px;letter-spacing:3px;font-weight:500}
.section-sub{position:absolute;top:214px;width:100%;text-align:center;font-size:12px;letter-spacing:4px;font-weight:600;color:#c9c9c9}
.service-card{position:absolute;top:292px;width:326px;height:500px;background:var(--white);border-radius:4px;text-align:center;color:var(--ink);padding:48px 36px 0}
.service-card::before{content:"";position:absolute;top:0;left:0;right:0;height:6px;background:var(--accent);border-radius:4px 4px 0 0}
.service-icon{width:60px;height:60px;border-radius:50%;background:var(--accent);margin:0 auto;display:flex;align-items:center;justify-content:center}
.service-name{font-size:22px;font-weight:600;margin-top:28px}
.service-text{font-size:15px;color:var(--muted);line-height:1.5;margin-top:50px}
.service-more{position:absolute;bottom:48px;left:36px;right:36px;padding-top:22px;border-top:1px solid #e6e6e6;color:var(--accent);font-size:13px;font-weight:700;letter-spacing:1px}

/* about */
.about{position:absolute;top:1560px;left:0;width:1200px;height:940px;background:var(--charcoal)}
.about-name{position:absolute;top:140px;left:96px;font-family:"Cormorant Garamond",serif;font-size:44px;font-weight:500;letter-spacing:2px}
.about-role{position:absolute;top:196px;left:96px;font-size:13px;letter-spacing:3px;color:#cfcfcf}
.about-social{position:absolute;top:224px;left:96px;display:flex;gap:12px}
.about-social span{width:14px;height:14px;border-radius:50%;background:#d8d8d8;display:block}
.about-body{position:absolute;top:258px;left:96px;width:600px}
.about-lead{font-size:24px;line-height:1.3;font-weight:600}
.about-body p{font-size:15px;line-height:1.5;color:#e0e0e0;margin-top:18px}
.about-body ul{margin:10px 0 0 22px;font-size:15px;line-height:1.5;color:#e0e0e0}
.about-body p.tight{margin-top:0}
.btn-outline{position:absolute;top:800px;left:96px;width:116px;height:34px;border:1px solid var(--white);border-radius:4px;font-size:12px;font-weight:700;letter-spacing:1px;display:flex;align-items:center;justify-content:center}
.portrait{position:absolute;top:80px;left:768px;width:368px;height:408px;background:linear-gradient(160deg,#f2f2f2 0%,#d9cfc6 50%,#b38a6a 100%);border-radius:4px}
.avatar{position:absolute;top:168px;left:722px;width:64px;height:64px;border-radius:50%;background:linear-gradient(160deg,#e8e4e0,#a77a5a);border:3px solid var(--white)}
.quote-panel{position:absolute;top:488px;left:768px;width:368px;height:432px;background:var(--panel);text-align:center;padding-top:56px}
.quote-mark{font-family:"Cormorant Garamond",serif;font-size:56px;line-height:.6;color:var(--white)}
.quote-text{font-size:16px;margin-top:24px;color:#eaeaea}
.quote-sign{font-family:"Cormorant Garamond",serif;font-style:italic;font-size:28px;color:var(--accent);margin-top:20px}
.dragonfly{position:absolute;left:150px;top:236px;width:150px;height:150px;border-radius:50%;background:radial-gradient(circle,#5a4a40 0%,rgba(51,51,51,0) 70%)}

/* help */
.help{position:absolute;top:2500px;left:0;width:1200px;height:400px;background:var(--charcoal-deep)}
.help-title{position:absolute;top:104px;left:28px;font-family:"Cormorant Garamond",serif;font-size:34px}
.help-text{position:absolute;top:152px;left:28px;width:300px;font-size:14px;line-height:1.45;color:#cfcfcf}
.help-link{position:absolute;top:204px;left:28px;font-size:16px;color:var(--accent);text-decoration:underline}
.help-list{position:absolute;top:118px;left:464px;list-style:none}
.help-list li{display:flex;align-items:center;gap:12px;font-size:14px;color:#e6e6e6;height:30px}
.consult-card{position:absolute;top:108px;left:720px;width:448px;height:264px;background:var(--white);border-radius:28px;padding:36px 40px;color:var(--ink)}
.consult-title{font-size:34px;color:var(--accent);font-weight:400}
.consult-note{font-size:14px;color:var(--muted);margin-top:6px}
.consult-call{display:flex;align-items:center;gap:18px;margin-top:34px}
.phone-dot{width:64px;height:64px;border-radius:50%;background:#111;display:flex;align-items:center;justify-content:center}
.call-label{font-size:13px;font-weight:600}
.call-number{font-size:34px;font-weight:600;letter-spacing:1px}

/* testimonial */
.testimonial{position:absolute;top:2900px;left:0;width:1200px;height:420px;background:linear-gradient(180deg,#e6b48a 0%,#efc49a 40%,#f3b27c 100%)}
.testimonial .mark{position:absolute;top:84px;width:100%;text-align:center;font-family:"Cormorant Garamond",serif;font-size:72px;color:var(--white);line-height:.6}
.testimonial-text{position:absolute;top:140px;width:100%;text-align:center;font-family:"Cormorant Garamond",serif;font-size:40px;line-height:1.25;font-weight:500;color:var(--white)}
.testimonial-author{position:absolute;top:262px;width:100%;text-align:center;font-size:13px;letter-spacing:3px;font-weight:700;color:var(--white)}
.arrow{position:absolute;top:196px}

/* footer */
.site-footer{position:absolute;top:3320px;left:0;width:1200px;height:100px;background:var(--charcoal);display:flex;align-items:center;justify-content:space-between;padding:0 80px 0 96px}
.site-footer small{font-size:13px;color:#bdbdbd}
.site-footer .social span{width:14px;height:14px}
</style>
</head>
<body>

<header class="site-header">
  <div class="brand">
    <div class="brand-name">Dr. June Tillard</div>
    <div class="brand-role">Licensed Psychologist</div>
  </div>
  <nav class="main-nav">
    <a class="active" href="#">WELCOME</a>
    <a href="#">SERVICES</a>
    <a href="#">ABOUT</a>
    <a href="#">FAQS</a>
    <a href="#">BLOG</a>
    <div class="social"><span></span><span></span><span></span></div>
  </nav>
</header>

<section class="hero">
  <div class="hero-photo" role="img" aria-label="Mountain lake at dusk between steep cliffs"></div>
  <div class="hero-copy">
    <h1 class="hero-title">Holistic Therapy</h1>
    <p class="hero-tagline">an integrative approach to transformation</p>
  </div>
</section>

<section class="services">
  <h2 class="section-title">SERVICES</h2>
  <p class="section-sub">GRIEF COUNSELING</p>

  <article class="service-card" style="left:96px">
    <div class="service-icon"><svg width="28" height="28" viewBox="0 0 24 24" fill="#fff"><circle cx="12" cy="7" r="4"/><path d="M4 21c0-5 4-8 8-8s8 3 8 8z"/></svg></div>
    <h3 class="service-name">Individual therapy</h3>
    <p class="service-text">Life can be challenging, and sometimes we all need someone to talk to. Individual therapy offers a safe, confidential space to explore your thoughts, feelings, and experiences</p>
    <div class="service-more">LEARN MORE</div>
  </article>

  <article class="service-card" style="left:438px">
    <div class="service-icon"><svg width="30" height="28" viewBox="0 0 26 24" fill="#fff"><circle cx="7" cy="6" r="3.5"/><circle cx="19" cy="6" r="3.5"/><path d="M2 22v-8c0-2 2-4 5-4s5 2 5 4v8zM14 22v-8c0-2 2-4 5-4s5 2 5 4v8z"/></svg></div>
    <h3 class="service-name">Couples therapy</h3>
    <p class="service-text">Relationships take work, and every couple faces challenges. Whether you're dealing with communication issues, trust concerns, intimacy struggles</p>
    <div class="service-more">LEARN MORE</div>
  </article>

  <article class="service-card" style="left:780px">
    <div class="service-icon"><svg width="30" height="28" viewBox="0 0 26 24" fill="#fff"><circle cx="6" cy="6" r="3"/><circle cx="20" cy="6" r="3"/><circle cx="13" cy="11" r="2.5"/><path d="M1 22v-7c0-2 2-4 5-4s4 1 4 3v8zM16 22v-8c0-2 1-3 4-3s5 2 5 4v7zM10 22v-4c0-2 1-3 3-3s3 1 3 3v4z"/></svg></div>
    <h3 class="service-name">Family counseling</h3>
    <p class="service-text">Families can face a variety of challenges - whether it's parenting struggles, generational conflicts, communication breakdowns, or adjusting to life changes</p>
    <div class="service-more">LEARN MORE</div>
  </article>
</section>

<section class="about">
  <h2 class="about-name">DR. JUNE TILLARD</h2>
  <p class="about-role">LICENSED CLINICAL PSYCHOLOGIST</p>
  <div class="about-social"><span></span><span></span><span></span><span></span></div>
  <div class="about-body">
    <p class="about-lead">are you struggling with issues that affect the way you live, love or work?</p>
    <p>Dr. June Tillard and her associates are licensed psychologists in Ashford, Ohio. We offer therapy for individuals, couples and families to help you create meaningful change, whether you</p>
    <ul>
      <li>Feel overwhelmed with depression or anxiety.</li>
      <li>Experience a lack of connection in your marriage.</li>
      <li>Worry excessively about what others think.</li>
      <li>Have a history of trauma or abuse.</li>
      <li>Parent a child with complex needs.</li>
      <li>Struggle with other life challenges</li>
    </ul>
    <p class="tight">We have extensive experience treating a full spectrum of mental health disorders using a collaborative and compassionate approach. In addition to individual therapy, we also provide couples counseling and family therapy.</p>
    <p>Dr. Tillard's practice, based in the West Ashford area of Dayton, is best suited for those who wish to deeply examine their inner world to gain insight, identify what matters most, and create lasting change towards a more fulfilling life.</p>
  </div>
  <div class="btn-outline">CONTACT</div>

  <div class="portrait" role="img" aria-label="Portrait photograph of the psychologist"></div>
  <div class="avatar" role="img" aria-label="Small round portrait photograph"></div>
  <div class="quote-panel">
    <div class="quote-mark">&ldquo;</div>
    <p class="quote-text">"Making sure you live your life to the fullest"</p>
    <p class="quote-sign">Dr June Tillard</p>
    <div class="dragonfly" role="img" aria-label="Line illustration of a dragonfly"></div>
  </div>
</section>

<section class="help">
  <h2 class="help-title">How can I help you?</h2>
  <p class="help-text">If you're experiencing any kind of mental illness or problem in relations.</p>
  <a class="help-link">Explore Programs</a>
  <ul class="help-list">
    <li><svg width="16" height="16" viewBox="0 0 16 16"><rect x="1" y="1" width="14" height="14" rx="2" fill="none" stroke="#f0643c" stroke-width="1.5"/><path d="M4 8l3 3 5-6" fill="none" stroke="#f0643c" stroke-width="1.5"/></svg>Family Problems</li>
    <li><svg width="16" height="16" viewBox="0 0 16 16"><rect x="1" y="1" width="14" height="14" rx="2" fill="none" stroke="#f0643c" stroke-width="1.5"/><path d="M4 8l3 3 5-6" fill="none" stroke="#f0643c" stroke-width="1.5"/></svg>Breakups</li>
    <li><svg width="16" height="16" viewBox="0 0 16 16"><rect x="1" y="1" width="14" height="14" rx="2" fill="none" stroke="#f0643c" stroke-width="1.5"/><path d="M4 8l3 3 5-6" fill="none" stroke="#f0643c" stroke-width="1.5"/></svg>Business Failure</li>
    <li><svg width="16" height="16" viewBox="0 0 16 16"><rect x="1" y="1" width="14" height="14" rx="2" fill="none" stroke="#f0643c" stroke-width="1.5"/><path d="M4 8l3 3 5-6" fill="none" stroke="#f0643c" stroke-width="1.5"/></svg>Stress Issues</li>
    <li><svg width="16" height="16" viewBox="0 0 16 16"><rect x="1" y="1" width="14" height="14" rx="2" fill="none" stroke="#f0643c" stroke-width="1.5"/><path d="M4 8l3 3 5-6" fill="none" stroke="#f0643c" stroke-width="1.5"/></svg>Online Sessions</li>
  </ul>
  <div class="consult-card">
    <h3 class="consult-title">Call for Consultation</h3>
    <p class="consult-note">20 minutes free for the first session</p>
    <div class="consult-call">
      <div class="phone-dot"><svg width="26" height="26" viewBox="0 0 24 24" fill="#fff"><path d="M6.6 10.8a15 15 0 0 0 6.6 6.6l2.2-2.2c.3-.3.7-.4 1-.2 1.1.4 2.3.6 3.6.6.6 0 1 .4 1 1V20c0 .6-.4 1-1 1C10.6 21 3 13.4 3 4c0-.6.4-1 1-1h3.5c.6 0 1 .4 1 1 0 1.3.2 2.5.6 3.6.1.3 0 .7-.2 1z"/></svg></div>
      <div>
        <div class="call-label">Call Now</div>
        <div class="call-number">410- 555- 0182</div>
      </div>
    </div>
  </div>
</section>

<section class="testimonial">
  <div class="mark">&ldquo;</div>
  <p class="testimonial-text">June is a life changer, having magical skills<br>for helping people with psychotherapy</p>
  <p class="testimonial-author">NORA BELL</p>
  <svg class="arrow" style="left:40px" width="20" height="36" viewBox="0 0 20 36"><path d="M17 2L3 18l14 16" fill="none" stroke="#fff" stroke-width="2.5"/></svg>
  <svg class="arrow" style="right:40px" width="20" height="36" viewBox="0 0 20 36"><path d="M3 2l14 16L3 34" fill="none" stroke="#fff" stroke-width="2.5"/></svg>
</section>

<footer class="site-footer">
  <small>© 2020 June S. Tillard, PsyD</small>
  <div class="social"><span></span><span></span><span></span><span></span></div>
</footer>

</body>
</html>
```